Exciting Personal Development Book Cover: FIND ZEN NOW!

Design a Book Cover for my personal development book.
Title: Find Zen Now!
Author: Marcus Telly
Tagline: A real-life solution to get unstuck and break free

My picture must make up the front cover as I need to build my brand and people should recognise me on book shelves. Bold and catchy. How you do it is up to you. There must be space for a short testimonial from a famous person who is currently reading my book. I uploaded a sample of what I made in Photoshop but I don't have design skills.

I've added a PDF of my book so you can read the chapter index and introduction to get a sense of the content.

Target Market(s)

Personal Development Self-Help Market

Industry/Entity Type

Personal Development

Font styles to use
Serif
Sans Serif

Requirements
Must have
• My picture as hero image on cover.
Nice to have
• Must have Title, Tagline and my author name. If possible ZEN stands for 'Zeal, Energy & Nerve' If there is a way to fit this somewhere great. If it's too much then it can go somewhere on the back.

```html
<!DOCTYPE html>
<html lang="en">
<head>
<meta charset="UTF-8">
<title>Find Zen Now! — Book Cover</title>
<link rel="stylesheet" href="https://fonts.googleapis.com/css2?family=Anton&family=Oswald:wght@500;700&family=Allura&display=swap">
<style>
  :root {
    --page-bg: #e9e9e9;
    --cover-slate: #4a4d50;
    --cover-slate-mid: #3c3f42;
    --cover-slate-dark: #26282a;
    --spine-slate: #353739;
    --zen-green: #7ed957;
    --zen-green-deep: #3fae2a;
    --zen-lime: #c6e04a;
    --splatter-green: rgba(126, 217, 87, .85);
    --grime: rgba(20, 20, 22, .55);
    --ink-white: #ffffff;
    --photo-light: #cfd0d1;
    --photo-mid: #8e9092;
  }
  * { box-sizing: border-box; margin: 0; padding: 0; }
  html, body {
    width: 1200px; height: 800px; overflow: hidden;
    background: var(--page-bg);
  }
  .book {
    position: absolute; left: 312px; top: 25px;
    width: 575px; height: 750px; display: flex;
    box-shadow: 0 18px 40px rgba(0,0,0,.25);
  }

  /* ---------- Spine ---------- */
  .spine {
    width: 75px; height: 100%; position: relative;
    background:
      radial-gradient(circle at 30% 62%, var(--splatter-green) 0 2px, transparent 3px),
      radial-gradient(circle at 70% 70%, var(--splatter-green) 0 1.5px, transparent 2.5px),
      radial-gradient(circle at 45% 83%, var(--splatter-green) 0 2px, transparent 3px),
      radial-gradient(circle at 60% 96%, var(--splatter-green) 0 2px, transparent 3px),
      radial-gradient(circle at 35% 40%, var(--grime) 0 2px, transparent 3px),
      radial-gradient(circle at 65% 52%, var(--grime) 0 3px, transparent 4px),
      linear-gradient(180deg, var(--spine-slate), var(--cover-slate-dark));
    border-right: 1px solid rgba(0,0,0,.4);
  }
  .spine-title, .spine-author {
    position: absolute; left: 50%; white-space: nowrap;
    transform: translate(-50%, -50%) rotate(90deg);
    font-family: "Oswald", sans-serif; font-weight: 700;
    letter-spacing: 12px; font-size: 22px;
  }
  .spine-title { top: 200px; color: var(--zen-green); }
  .spine-author { top: 590px; color: var(--ink-white); }

  /* ---------- Front cover ---------- */
  .cover {
    position: relative; width: 500px; height: 100%; overflow: hidden;
    background:
      radial-gradient(ellipse 120px 80px at 22% 18%, rgba(255,255,255,.06), transparent),
      radial-gradient(ellipse 160px 90px at 70% 60%, rgba(0,0,0,.18), transparent),
      radial-gradient(ellipse 140px 110px at 30% 70%, rgba(255,255,255,.05), transparent),
      radial-gradient(ellipse 200px 120px at 80% 15%, rgba(0,0,0,.15), transparent),
      radial-gradient(ellipse at 40% 35%, var(--cover-slate) 0%, var(--cover-slate-mid) 50%, var(--cover-slate-dark) 100%);
  }
  .grime {
    position: absolute; inset: 0; pointer-events: none;
    background:
      radial-gradient(circle at 12% 8%, var(--grime) 0 3px, transparent 4px),
      radial-gradient(circle at 48% 5%, var(--grime) 0 2px, transparent 3px),
      radial-gradient(circle at 8% 34%, var(--grime) 0 2px, transparent 3px),
      radial-gradient(circle at 40% 46%, var(--grime) 0 4px, transparent 5px),
      radial-gradient(circle at 20% 58%, var(--grime) 0 3px, transparent 4px),
      radial-gradient(circle at 55% 67%, var(--grime) 0 2px, transparent 3px),
      radial-gradient(circle at 10% 80%, var(--grime) 0 2px, transparent 3px),
      radial-gradient(circle at 36% 88%, var(--grime) 0 3px, transparent 4px);
  }
  .splatter {
    position: absolute; inset: 0; pointer-events: none;
    background:
      radial-gradient(circle at 43% 54%, var(--splatter-green) 0 3px, transparent 5px),
      radial-gradient(circle at 47% 57%, var(--splatter-green) 0 2px, transparent 4px),
      radial-gradient(circle at 39% 59%, var(--splatter-green) 0 2.5px, transparent 4px),
      radial-gradient(circle at 51% 52%, var(--splatter-green) 0 1.5px, transparent 3px),
      radial-gradient(circle at 33% 63%, var(--splatter-green) 0 2px, transparent 4px),
      radial-gradient(circle at 12% 68%, var(--splatter-green) 0 2px, transparent 4px),
      radial-gradient(circle at 24% 73%, var(--splatter-green) 0 1.5px, transparent 3px),
      radial-gradient(circle at 6% 92%, var(--splatter-green) 0 2px, transparent 4px),
      radial-gradient(circle at 16% 97%, var(--splatter-green) 0 1.5px, transparent 3px),
      radial-gradient(circle at 41% 94%, var(--splatter-green) 0 2px, transparent 4px);
  }
  .author-photo {
    position: absolute; right: 0; top: 60px; width: 250px; height: 450px;
    background: radial-gradient(ellipse 60% 55% at 55% 45%, rgba(207,208,209,.75) 0%, rgba(142,144,146,.45) 50%, rgba(60,63,66,0) 100%);
  }

  .title-script {
    position: absolute; left: 28px; top: 36px; z-index: 2;
    font-family: "Allura", cursive; font-size: 96px; line-height: 1;
    color: var(--ink-white);
  }
  .title-zen {
    position: absolute; left: 50px; top: 100px; z-index: 1;
    font-family: "Anton", sans-serif; font-size: 200px; line-height: 1;
    background: linear-gradient(135deg, var(--zen-green-deep) 0%, var(--zen-green) 45%, var(--zen-lime) 100%);
    -webkit-background-clip: text; background-clip: text; color: transparent;
  }
  .title-now {
    position: absolute; left: 156px; top: 338px;
    font-family: "Anton", sans-serif; font-size: 88px; line-height: 1;
    color: var(--ink-white);
  }
  .tagline {
    position: absolute; right: 20px; top: 520px; width: 230px;
    font-family: "Oswald", sans-serif; font-weight: 700;
    font-size: 12.5px; letter-spacing: 2.2px; line-height: 1.4;
    text-transform: uppercase; color: var(--zen-green); text-align: center;
  }
  .tagline .lead { color: var(--ink-white); }
  .author-name {
    position: absolute; left: 30px; top: 548px;
    font-family: "Anton", sans-serif; font-weight: 400; font-size: 70px; line-height: .92;
    color: var(--ink-white); text-transform: uppercase;
  }
  .testimonial {
    position: absolute; left: 30px; right: 20px; bottom: 24px;
    font-family: "Oswald", sans-serif; font-weight: 500;
    font-size: 14px; letter-spacing: 1px; color: var(--ink-white);
  }
</style>
</head>
<body>
  <div class="book">
    <div class="spine">
      <span class="spine-title">FIND ZEN NOW</span>
      <span class="spine-author">MARCUS TELLY</span>
    </div>
    <div class="cover">
      <div class="grime"></div>
      <div class="author-photo" role="img" aria-label="Portrait photo of author Marcus Telly smiling in a white open-collar shirt"></div>
      <div class="splatter"></div>
      <div class="title-script">Find</div>
      <div class="title-zen">ZEN</div>
      <div class="title-now">NOW!</div>
      <p class="tagline"><span class="lead">Stacking</span><br>Zeal, Energy and Nerve<br>to overcome pain and the obstacles of life</p>
      <h2 class="author-name">Marcus<br>Telly</h2>
      <p class="testimonial">Occus, quiaess itaspiti doluptas alit et volo.' -Name Surname</p>
    </div>
  </div>
</body>
</html>
```